Visitenkarten-Design für ein Beratungsunternehmen im Immobilienbereich
Zielgruppe
Wir sind ein Beratungsunternehmen im Immobilienbereich. Von der Planung, Ingenieuring, bis hin zum Vertriebskonzept
Aufgabenstellung
Das vorhandene Logo mit den zugehörigen Farben und Schriften
Firmennamen: FORLAN
Name: Jörg Tannhuber
Geschäftsführer
Anschrift: Lindenhofweg 14, 64683 Einhausen
What3word: ///kiesel.wolken.taschen
Telefon: +49 6251 4710562
Mobil: +49 162 5074831
Mail: kontakt@forlan-beispiel.immo
Web: www.forlan-beispiel.immo
Slogan: Für Ihren MehrWert
Das Logo soll als Prägung und teilweise in silber/ heissfolie ausgeführt werden.

```html
<!DOCTYPE html>
<html lang="de">
<head>
<meta charset="utf-8">
<title>FORLAN Visitenkarte</title>
<link href="https://fonts.googleapis.com/css2?family=Montserrat:wght@600&family=Quicksand:wght@300;400&display=swap" rel="stylesheet">
<style>
  :root {
    --stage: #dcdde0;
    --navy: #262d63;
    --navy-deep: #1f2553;
    --silver: #c9ccd4;
    --silver-soft: #aeb3c2;
    --text-light: #d4d7e0;
  }
  * { margin: 0; padding: 0; box-sizing: border-box; }
  html, body { width: 1200px; height: 675px; overflow: hidden; }
  body {
    background: var(--stage);
    position: relative;
    font-family: "Quicksand", sans-serif;
  }
  .card {
    position: absolute;
    top: 176px;
    width: 510px;
    height: 324px;
    background: linear-gradient(160deg, var(--navy), var(--navy-deep));
    border-radius: 3px;
    box-shadow: 0 8px 24px rgba(0,0,0,.18);
    color: var(--text-light);
  }
  .card--front { left: 60px; }
  .card--back { left: 630px; }

  .brand-name {
    font-family: "Montserrat", sans-serif;
    font-weight: 600;
    color: var(--silver);
    letter-spacing: 4px;
    white-space: nowrap;
  }
  .card--front .brand-name {
    position: absolute; top: 92px; left: 0; right: 0;
    text-align: center; font-size: 60px;
  }
  .card--front .website {
    position: absolute; top: 214px; left: 0; right: 0;
    text-align: center; font-size: 20px; letter-spacing: 6px;
    font-weight: 400; white-space: nowrap;
  }

  .card--back .brand-name {
    position: absolute; top: 36px; left: 150px; font-size: 50px;
  }
  .logo-rule {
    position: absolute; top: 112px; left: 120px; width: 360px; height: 1px;
    background: linear-gradient(90deg, transparent, var(--silver-soft));
  }
  .slogan {
    position: absolute; top: 136px; left: 40px;
    font-family: "Montserrat", sans-serif; font-weight: 600;
    font-size: 13px; letter-spacing: 1px; color: var(--silver);
    white-space: nowrap;
  }
  .person {
    position: absolute; top: 122px; right: 30px; text-align: right;
    white-space: nowrap;
  }
  .person__name { font-size: 21px; font-weight: 400; }
  .person__role { font-size: 14px; font-weight: 300; }
  .contact-list {
    position: absolute; right: 30px; top: 178px;
    list-style: none; text-align: right; font-size: 12px; font-weight: 300;
    white-space: nowrap;
  }
  .contact-list li, .address-list li {
    display: flex; align-items: center; gap: 6px; line-height: 18px;
  }
  .contact-list li { justify-content: flex-end; }
  .divider {
    position: absolute; top: 226px; left: 30px; width: 450px; height: 1px;
    background: linear-gradient(90deg, var(--silver-soft), rgba(174,179,194,.2));
  }
  .address-list {
    position: absolute; left: 30px; top: 242px;
    list-style: none; font-size: 13px; font-weight: 300;
    white-space: nowrap;
  }
  .address-list .indent { padding-left: 20px; }
  .icon { width: 13px; height: 13px; flex: none; stroke: var(--text-light); fill: none; stroke-width: 1.2; }
</style>
</head>
<body>
  <section class="card card--front">
    <div class="brand-name">FORLAN</div>
    <div class="website">www.forlan-beispiel.immo</div>
  </section>

  <section class="card card--back">
    <div class="brand-name">FORLAN</div>
    <div class="logo-rule"></div>
    <div class="slogan">FÜR IHREN MEHRWERT</div>
    <div class="person">
      <div class="person__name">Jörg Tannhuber</div>
      <div class="person__role">Geschäftsführer</div>
    </div>
    <ul class="contact-list">
      <li>+49 162 5074831
        <svg class="icon" viewBox="0 0 14 14"><rect x="4" y="1" width="6" height="12" rx="1"/><line x1="6" y1="11" x2="8" y2="11"/></svg>
      </li>
      <li>kontakt@forlan-beispiel.immo
        <svg class="icon" viewBox="0 0 14 14"><rect x="1" y="3" width="12" height="8"/><polyline points="1,3 7,8 13,3"/></svg>
      </li>
    </ul>
    <div class="divider"></div>
    <ul class="address-list">
      <li>
        <svg class="icon" viewBox="0 0 14 14"><polyline points="1,7 7,2 13,7"/><polyline points="3,6 3,12 11,12 11,6"/></svg>
        Lindenhofweg 14,
      </li>
      <li class="indent">64689 Lorschbach</li>
      <li>
        <svg class="icon" viewBox="0 0 14 14"><rect x="1.5" y="1.5" width="11" height="11"/></svg>
        ///kiesel.wolken.taschen
      </li>
      <li>
        <svg class="icon" viewBox="0 0 14 14"><path d="M3 1.5l2.2 2.6-1.3 1.5a7 7 0 0 0 4.5 4.5l1.5-1.3 2.6 2.2-1.5 1.5A10 10 0 0 1 1.5 3z"/></svg>
        +49 6251 4710562
      </li>
    </ul>
  </section>
</body>
</html>
```